Hair and Wellness Brochure and Pricelist design

I am requiring a brochure that has a fresh, though alternative design. My business name is The Quiet Harbour Hair and Wellness. I have a very professional approach to my work and love to give that little bit extra to all of my clients. My passion for health, has led me to channel my business alternatively by using non toxic colours and styling products and through that same vein, I have studied Aromatherapy, Indian Head Massage and Reiki...all additional services I use where required.
My studio has very neutral tones of beige,white and beech wood but these tones aren't necessarily required for the brochure.I like to create a space of calm, peace and quiet, where my clients feel refreshed and rejuvenated..

Industry/Entity Type

Business

```html
<!DOCTYPE html>
<html lang="en">
<head>
<meta charset="utf-8">
<title>The Quiet Harbour Hair and Wellness – Brochure Cover</title>
<link rel="stylesheet" href="https://fonts.googleapis.com/css2?family=Open+Sans:wght@400&display=swap">
<style>
  :root {
    --cocoa: #6a4a3d;
    --cocoa-deep: #5f4135;
    --taupe: #a48b80;
    --taupe-light: #c4b1a7;
    --mist: #d9cbc3;
    --cream: #f3efdc;
    --text-light: #f4ece6;
    --swirl: #b59c92;
  }
  * { margin: 0; padding: 0; box-sizing: border-box; }
  html, body {
    width: 1200px;
    height: 2770px;
    overflow: hidden;
    background: var(--cocoa);
  }
  .brochure-cover {
    position: relative;
    width: 1200px;
    height: 2770px;
    background: var(--cocoa);
    overflow: hidden;
    font-family: "Open Sans", Arial, sans-serif;
  }
  .lily-pattern {
    position: absolute;
    inset: 0;
    background:
      radial-gradient(circle at 30% 40%, rgba(255,255,255,0.035), transparent 60%),
      radial-gradient(circle at 75% 70%, rgba(255,255,255,0.03), transparent 55%);
  }
  .header-waves {
    position: absolute;
    top: 0;
    left: 0;
    width: 1200px;
    height: 340px;
    display: block;
  }
  .brand-name {
    position: absolute;
    top: 800px;
    left: 0;
    width: 1200px;
    text-align: center;
    color: var(--cream);
    font-weight: 400;
    line-height: 1.15;
  }
  .brand-name .brand-main {
    display: block;
    font-size: 118px;
    letter-spacing: 2px;
  }
  .brand-name .brand-sub {
    display: block;
    margin-top: 18px;
    font-size: 44px;
    letter-spacing: 10px;
  }
  .services-line {
    position: absolute;
    top: 1568px;
    left: 0;
    width: 1200px;
    text-align: center;
    color: var(--text-light);
    font-size: 50px;
    font-weight: 400;
    letter-spacing: 0.5px;
  }
  .swirl-ornament {
    position: absolute;
    left: 180px;
    top: 2060px;
    width: 1020px;
    height: 710px;
    background: radial-gradient(ellipse at 75% 65%, rgba(181,156,146,0.55), rgba(181,156,146,0.18) 55%, transparent 75%);
  }
</style>
</head>
<body>
  <main class="brochure-cover">
    <div class="lily-pattern" role="img" aria-label="Faint repeating lily flower pattern across the background"></div>

    <svg class="header-waves" viewBox="0 0 1200 340" aria-hidden="true">
      <rect x="0" y="0" width="1200" height="340" fill="var(--cocoa)"/>
      <path d="M0 0 H1200 V130 C900 170 450 250 0 290 Z" fill="var(--taupe)"/>
      <path d="M0 0 H1200 V60 C850 110 420 170 0 210 Z" fill="var(--taupe-light)"/>
      <path d="M0 0 H1200 V20 C820 40 400 90 0 130 Z" fill="var(--mist)" opacity="0.6"/>
    </svg>

    <h1 class="brand-name">
      <span class="brand-main">The Quiet Harbour</span>
      <span class="brand-sub">Hair and Wellness</span>
    </h1>

    <p class="services-line">Aromatherapy, Indian Head Massage and Reiki</p>

    <div class="swirl-ornament" role="img" aria-label="Decorative flowing swirl ornament rising from the lower right corner"></div>
  </main>
</body>
</html>
```